Stationery for use with Ninefold Ridge reports

I would like to get a stationery design that my firm -- Ninefold Ridge Advisory -- will use as a format for reports that we send our clients. I am specifically looking for a design for use on a piece of paper or letterhead -- not business cards or envelopes.

We are an Africa based US risk intelligence and strategy firm that works with multinational corporations operating in West Africa. Our initial thinking is that we would like a color scheme consistent with our existing logo -- however we are open to other color schemes.

Also, we would like to see at least two separate versions: one with our company name and logo, the other without name and logo.

We also would like font recommendations for the stationary design.

The final design should communicate discreet professionalism and a modern approach, but it should not overshadow the words and information printed on the stationery.

Target Market(s)

Multinational corporations that currently use our products.

Font styles to use
Serif
Sans Serif

Requirements
Must have
• Sense of discreet professionalism that will not overshadow the content we put onto the stationery format.
• We would like to see designs with and without our company name/logo.
• Please suggest fonts that would work with the stationery.
Nice to have
• Ideally colors consistent with out existing logo, though we are open to and even encourage other ideas.
Should not have
• No need for business cards or envelopes.

```html
<!DOCTYPE html>
<html lang="en">
<head>
<meta charset="utf-8">
<title>Ninefold Ridge Advisory — Letterhead</title>
<link rel="stylesheet" href="https://fonts.googleapis.com/css2?family=Arimo:wght@400;700&display=swap">
<style>
  :root {
    --backdrop: #e2e2e2;
    --paper-top: #ffffff;
    --paper-bottom: #f0f0f0;
    --ink: #4a4a4a;
    --ink-soft: #555555;
    --brand: #1f3a4a;
    --rule: #9a9a9a;
    --signature: #2b2b2b;
  }
  * { margin: 0; padding: 0; box-sizing: border-box; }
  html, body {
    width: 1200px; height: 1141px; overflow: hidden;
    background: var(--backdrop);
    font-family: "Arimo", Helvetica, Arial, sans-serif;
    color: var(--ink);
  }
  .letterhead {
    position: absolute; left: 208px; top: 20px;
    width: 783px; height: 1101px;
    background: linear-gradient(160deg, var(--paper-top) 30%, var(--paper-bottom) 100%);
    box-shadow: 0 2px 6px rgba(0,0,0,0.18);
  }
  .brand {
    position: absolute; left: 59px; top: 112px;
    display: flex; align-items: center; gap: 9px;
    color: var(--brand); font-weight: 700;
  }
  .brand-dot { width: 14px; height: 14px; border-radius: 50%; background: var(--brand); }
  .brand-name { font-size: 20px; line-height: 1.15; letter-spacing: 0.3px; }
  .contact {
    position: absolute; top: 129px; right: 57px;
    display: flex; font-size: 11.4px; line-height: 15px; color: var(--ink-soft);
  }
  .contact-address { text-align: right; padding-right: 10px; border-right: 1px solid var(--rule); }
  .contact-lines { padding-left: 10px; }
  .contact-line { display: flex; align-items: center; gap: 6px; }
  .contact-line svg { width: 10px; height: 10px; fill: var(--brand); }
  .greeting {
    position: absolute; left: 59px; top: 272px;
    font-size: 19px; color: var(--ink);
  }
  .body-copy {
    position: absolute; left: 59px; top: 331px; width: 667px;
    font-size: 11.2px; line-height: 16.7px; text-align: justify;
  }
  .body-copy p { margin-bottom: 16.5px; }
  .closing { position: absolute; left: 58px; top: 700px; font-size: 11.2px; }
  .signature-area {
    position: absolute; left: 54px; top: 740px; width: 226px; height: 64px;
    background: linear-gradient(90deg, rgba(43,43,43,0.10), rgba(43,43,43,0.04));
    border-radius: 4px;
  }
</style>
</head>
<body>
  <div class="letterhead">
    <div class="brand">
      <span class="brand-dot"></span>
      <span class="brand-name">Ninefold Ridge<br>Advisory</span>
    </div>

    <div class="contact">
      <div class="contact-address">
        2210 Harbor View Road<br>
        Fairhaven, Oregon 97180<br>
        www.ninefoldridge.com
      </div>
      <div class="contact-lines">
        <div class="contact-line">
          <svg viewBox="0 0 24 24" aria-hidden="true"><path d="M6.6 10.8a15.1 15.1 0 0 0 6.6 6.6l2.2-2.2c.3-.3.7-.4 1-.2 1.1.4 2.3.6 3.6.6.6 0 1 .4 1 1V20c0 .6-.4 1-1 1A17 17 0 0 1 3 4c0-.6.4-1 1-1h3.5c.6 0 1 .4 1 1 0 1.3.2 2.5.6 3.6.1.3 0 .7-.2 1z"/></svg>
          555-014-2280
        </div>
        <div class="contact-line">
          <svg viewBox="0 0 24 24" aria-hidden="true"><path d="M6 2h12v6H6zM3 9h18a1 1 0 0 1 1 1v7h-4v5H6v-5H2v-7a1 1 0 0 1 1-1zm5 7v4h8v-4z"/></svg>
          555-014-2291
        </div>
        <div class="contact-line">
          <svg viewBox="0 0 24 24" aria-hidden="true"><path d="M2 5h20v14H2zm2 2v.5l8 5 8-5V7l-8 5z"/></svg>
          info@ninefoldridge.com
        </div>
      </div>
    </div>

    <h1 class="greeting" style="font-weight:400">Dear Mr. Carver,</h1>

    <div class="body-copy">
      <p>Lorem ipsum dolor sit amet, consectetur adipiscing elit. Donec orci purus, luctus vitae dignissim eu, iaculis sed purus. Vivamus faucibus, ipsum nec aliquet viverra, leo mauris condimentum ligula, sit amet sagittis enim ligula quis arcu. Nam egestas tortor id nisi porttitor mattis. In tortor ante, ultricies in suscipit a, tempus non massa. Vivamus et auctor mi. Fusce vel massa nulla. Phasellus nec eros mauris, et scelerisque orci.</p>
      <p>Donec malesuada orci vitae nulla accumsan porta a id massa. Quisque accumsan iaculis magna sit amet fringilla. Maecenas consequat, magna eget tincidunt semper, odio nibh rutrum mi, id feugiat ante nisi eu risus. Vestibulum nunc orci, rhoncus a placerat in, ultricies in mi. Cras mattis varius eros, vel fringilla nisi suscipit eget. Quisque scelerisque sagittis nulla at porttitor.</p>
      <p>Sed id augue vitae urna euismod commodo aliquet a quam. Pellentesque arcu velit, cursus et malesuada ut, consequat et diam. Nullam erat sem, rhoncus id ullamcorper vitae, rhoncus et arcu. In ultricies ultricies nulla, ut rutrum nisi iaculis at. Donec eu magna a metus ornare faucibus. Fusce aliquet faucibus ultricies. Morbi semper, est id tincidunt gravida, sem arcu adipiscing lacus, ac bibendum nulla leo eu purus. Quisque nec diam sed risus consectetur a ccumsan quis quis nibh. Vestibulum id purus lorem.</p>
      <p>It is a long established fact that a reader will be distracted by the readable content of a page when looking at its layout. The point of using Lorem Ipsum is that it has a more-or-less normal distribution of letters, as opposed to using 'Content here, content here', making it look like readable English. Many desktop publishing packages</p>
      <p>ada ut, consequat et diam. Nullam erat sem, rhoncus id ullamcorper vitae, rhoncus et arcu. In ultricies ultricies nulla, ut rutrum nisi iaculis at. Donec eu magna a metus ornare faucibus. Fusce aliquet faucibus ultricies. Morbi semper,</p>
    </div>

    <div class="closing">Sincerely,</div>
    <div class="signature-area" role="img" aria-label="Handwritten signature of the sender"></div>
  </div>
</body>
</html>
```